Quillory Nest Business Card

I need a business card design. We are a collaborate online training company. Our colors are gray and green. Our website is QuilloryNest.com

I would like an area for a profile picture within the card

```html
<!DOCTYPE html>
<html lang="en">
<head>
<meta charset="utf-8">
<title>Quillory Nest Business Card</title>
<link href="https://fonts.googleapis.com/css2?family=Open+Sans:wght@400;600;700&display=swap" rel="stylesheet">
<style>
  :root {
    --stage: #3a3a3a;
    --green: #8cc63f;
    --green-deep: #6aa52c;
    --green-soft: #a4d45e;
    --ink: #1b1b1b;
    --gray: #4a4a4a;
    --paper: #ffffff;
    --paper-shade: #eeeeee;
    --photo-warm: #d9b77c;
    --photo-light: #f1e3b8;
  }
  * { box-sizing: border-box; margin: 0; padding: 0; }
  html, body { width: 1200px; height: 834px; overflow: hidden; }
  body {
    background: var(--stage);
    font-family: "Open Sans", Arial, sans-serif;
    position: relative;
  }
  .card {
    position: absolute;
    top: 262px;
    width: 540px;
    height: 309px;
    border-radius: 3px;
    overflow: hidden;
    box-shadow: 0 12px 30px rgba(0,0,0,.45);
  }
  /* Front */
  .card-front {
    left: 40px;
    background: linear-gradient(135deg, var(--green-soft), var(--green) 50%, var(--green-deep));
  }
  .front-backdrop {
    position: absolute; inset: 0;
    background: radial-gradient(ellipse at 55% 45%, rgba(255,255,255,.18), rgba(255,255,255,0) 65%);
  }
  .front-brand {
    position: absolute; left: 40px; top: 54px;
    display: flex; align-items: center; gap: 12px;
    color: var(--paper);
    font-weight: 700; font-size: 38px; letter-spacing: -.5px;
  }
  .brand-dot {
    width: 30px; height: 30px; border-radius: 50%;
    background: currentColor; flex: none;
  }
  .photo-row {
    position: absolute; left: 150px; right: 24px; bottom: 30px;
    display: flex; justify-content: space-between;
  }
  .profile-photo {
    width: 112px; height: 112px; border-radius: 50%;
    border: 4px solid var(--paper);
    background: radial-gradient(circle at 40% 35%, var(--photo-light), var(--photo-warm) 70%, #b58d4f);
  }
  /* Back */
  .card-back {
    left: 620px;
    background: linear-gradient(160deg, var(--paper), var(--paper) 55%, var(--paper-shade));
    color: var(--gray);
  }
  .back-brand {
    position: absolute; right: 56px; top: 46px;
    display: flex; align-items: center; gap: 10px;
    color: var(--ink);
    font-weight: 700; font-size: 32px; letter-spacing: -.5px;
  }
  .back-brand .brand-dot { background: var(--green); width: 26px; height: 26px; }
  .divider {
    position: absolute; left: 40px; right: 40px; top: 150px;
    height: 2px; background: var(--green);
  }
  .holder { position: absolute; left: 40px; top: 110px; }
  .holder-name { font-weight: 700; font-size: 17px; color: var(--ink); line-height: 1.2; }
  .holder-role { font-size: 13px; color: var(--green); line-height: 1.3; }
  .contact-list {
    position: absolute; right: 40px; top: 168px;
    list-style: none; text-align: right;
    font-size: 12.5px; line-height: 21px; color: var(--gray);
  }
  .contact-list li { display: flex; justify-content: flex-end; align-items: center; gap: 10px; }
  .contact-list svg { width: 12px; height: 12px; fill: none; stroke: var(--green); stroke-width: 1.6; }
  .address {
    position: absolute; left: 40px; bottom: 34px;
    font-size: 13px; line-height: 20px; color: var(--gray);
  }
</style>
</head>
<body>
  <section class="card card-front">
    <div class="front-backdrop" role="img" aria-label="Soft green-toned photo of a person working on a laptop"></div>
    <div class="front-brand"><span class="brand-dot"></span>Quillory Nest</div>
    <div class="photo-row">
      <div class="profile-photo" role="img" aria-label="Profile photo"></div>
      <div class="profile-photo" role="img" aria-label="Profile photo"></div>
      <div class="profile-photo" role="img" aria-label="Profile photo"></div>
    </div>
  </section>

  <section class="card card-back">
    <div class="back-brand"><span class="brand-dot"></span>Quillory Nest</div>
    <div class="holder">
      <p class="holder-name">Dalen Marsh</p>
      <p class="holder-role">Owner</p>
    </div>
    <div class="divider"></div>
    <ul class="contact-list">
      <li>(555) 204-7719
        <svg viewBox="0 0 12 12"><path d="M2 4c0-1 1-2 4-2s4 1 4 2v1H8V4H4v1H2z M3 6h6l1 4H2z"/></svg></li>
      <li>(555) 204-7719
        <svg viewBox="0 0 12 12"><rect x="3" y="1" width="6" height="10" rx="1"/><path d="M5.5 9h1"/></svg></li>
      <li>email@quillorynest.com
        <svg viewBox="0 0 12 12"><rect x="1" y="3" width="10" height="7"/><path d="M1 3l5 4 5-4"/></svg></li>
      <li>www.quillorynest.com
        <svg viewBox="0 0 12 12"><circle cx="6" cy="6" r="5"/><path d="M1 6h10M6 1c-3 3-3 7 0 10M6 1c3 3 3 7 0 10"/></svg></li>
    </ul>
    <p class="address">880 Larkmoor Ave. Suite 4<br>Fenwick, Ohio 40912</p>
  </section>
</body>
</html>
```